Business Card Design

Harlow Sun and Electrical is a new company that specializes in solar pv. I need a card with similar attributes to the ones I have attached. I am after a two sided card with the logo on one side and the logo plus info on the other. I would prefer one side to be black and the other to be a colour but am open to suggestions. The colour scheme I was thinking of was blue or green. I plan on spot glossing the logos if that makes any difference. I have attached a file of my logo in a few colours, none of which I am completely sold on so please feel free to change colous to suit.
Thanks.
Contact Information for Business Card
Dorian Harlow, www.hwx-example.net.nz, dorian@hwx-example.net.nz, t. 0508 4 BRIGHT m. 027469318

```html
<!DOCTYPE html>
<html lang="en">
<head>
<meta charset="utf-8">
<title>Harlow Sun and Electrical – Business Card</title>
<link href="https://fonts.googleapis.com/css2?family=Open+Sans:wght@400;600;700&display=swap" rel="stylesheet">
<style>
  :root {
    --bg: #c4c8ce;
    --card: #ffffff;
    --green: #8dc63f;
    --orange: #f5a431;
    --blue: #1b75bb;
    --teal: #1f6f8b;
    --ink: #2e3a2a;
    --font: "Open Sans", Arial, sans-serif;
  }
  * { margin: 0; padding: 0; box-sizing: border-box; }
  html, body { width: 1200px; height: 866px; overflow: hidden; }
  body {
    background: var(--bg);
    font-family: var(--font);
    display: flex;
    align-items: center;
    justify-content: center;
    gap: 40px;
  }
  .card {
    position: relative;
    width: 540px;
    height: 310px;
    background: var(--card);
    box-shadow: 0 6px 18px rgba(0,0,0,.18);
    overflow: hidden;
  }
  .card__art { position: absolute; inset: 0; width: 100%; height: 100%; }
  .logo {
    position: absolute;
    display: flex;
    flex-direction: column;
    align-items: center;
    text-align: center;
    gap: 8px;
  }
  .logo__mark {
    width: 34px; height: 34px;
    background: var(--blue);
    flex: none;
  }
  .logo__name {
    font-family: var(--font);
    font-weight: 600;
    color: var(--teal);
    font-size: 18px;
    line-height: 1.25;
    letter-spacing: .5px;
  }
  .card--front .logo { left: 50%; top: 50%; transform: translate(-50%, -50%); }
  .card--back .logo { left: 12px; top: 168px; width: 118px; gap: 6px; }
  .card--back .logo__mark { width: 26px; height: 26px; }
  .card--back .logo__name { font-size: 12.5px; letter-spacing: .3px; }
  .details {
    position: absolute;
    right: 26px;
    top: 26px;
    text-align: right;
    color: var(--ink);
    font-size: 12.5px;
    line-height: 1.35;
  }
  .details__name { font-weight: 700; font-size: 15px; }
  .details__role { font-size: 14px; margin-bottom: 44px; }
  .details__address { margin-bottom: 16px; }
  .details__line { display: flex; justify-content: flex-end; align-items: center; gap: 5px; }
  .icon { width: 11px; height: 11px; fill: var(--ink); }
</style>
</head>
<body>
  <section class="card card--front" aria-label="Card front">
    <div class="logo">
      <span class="logo__mark"></span>
      <span class="logo__name">Harlow Sun<br>and Electrical</span>
    </div>
  </section>

  <section class="card card--back" aria-label="Card back">
    <svg class="card__art" viewBox="0 0 540 310" aria-hidden="true">
      <path d="M0,0 L540,0 L540,310 L150,310 C175,180 120,40 0,0 Z" fill="var(--green)"/>
      <path d="M0,0 C110,12 178,90 150,310 L140,310 C165,110 100,22 0,6 Z" fill="var(--orange)"/>
      <path d="M0,6 C100,22 165,110 140,310 L134,310 C158,115 95,28 0,12 Z" fill="#ffffff"/>
      <path d="M150,112 C178,170 182,250 166,310 L192,310 C204,240 190,165 150,112 Z" fill="var(--blue)"/>
    </svg>

    <div class="logo">
      <span class="logo__mark"></span>
      <span class="logo__name">Harlow Sun<br>and Electrical</span>
    </div>

    <div class="details">
      <p class="details__name">Lennox Vare-Pryce</p>
      <p class="details__role">Consultant</p>
      <p class="details__address">042.9th floor,Quay<br>Harbour Road KTV</p>
      <p class="details__line">021 555 0147
        <svg class="icon" viewBox="0 0 24 24"><path d="M6.6 10.8a15.2 15.2 0 0 0 6.6 6.6l2.2-2.2c.3-.3.7-.4 1-.2 1.1.4 2.3.6 3.6.6.6 0 1 .4 1 1V20c0 .6-.4 1-1 1A17 17 0 0 1 3 4c0-.6.4-1 1-1h3.5c.6 0 1 .4 1 1 0 1.3.2 2.5.6 3.6.1.3 0 .7-.2 1z"/></svg>
      </p>
      <p class="details__line">021 555 0148
        <svg class="icon" viewBox="0 0 24 24"><path d="M6 2h9v6H6zM4 9h16v11H4zm3 3v2h3v-2zm5 0v2h3v-2zm-5 4v2h3v-2zm5 0v2h3v-2z"/></svg>
      </p>
      <p class="details__line">hello@example-mail.com
        <svg class="icon" viewBox="0 0 24 24"><path d="M2 5h20v14H2zm2 2v.5l8 5 8-5V7z"/></svg>
      </p>
      <p class="details__line">www.yoursite-example.com</p>
    </div>
  </section>
</body>
</html>
```